Web Design Project

Hi everyone

Thanks for taking the time to read about this project.

Website needed for Corvel, female singer/songwriter and performer who is launching her debut album this year. She writes and performs folk/pop/soft rock music and plays guitar and piano.

see vidrelay links for examples of Corvel's style:
http://www.vidrelay.example/watch?v=Qp3TzL8wRn2
http://www.vidrelay.example/watch?v=Hk7DbVu4sYe

Looking for a classy, modern feel to the website. Cool colours are preferred but open to ideas. It needs it to have CoinTrove set up so items can be purchased from the site. The theme will be continued to Friendspace and business cards.

Examples include:

http://www.belindacrosshaw.example/

http://tessavorlund.example/

http://www.juneqtunes.example/home

Pages and content to be included:

HOME - main picture and general content

BIO - written content about Corvel

NEWS - this will be regularly updated, blog style

GIGS - this will be regularly updated

GALLERY - content will be photos only

SEE AND HEAR - content will be Videos and audios

STORE - this will have a cointrove function for purchase of CD and merchandise

GENEROSITY - this page will be devoted to charity work and updated regularly

CONTACT - information on how to contact Corvel's management

Buttons will need to provide links to VidRelay, Chirpline, Friendspace, Snapwell

I will work closely with the designers in giving feedback as ideas are generated and then provide further content such as photos and videos.

Thanks for considering this project!
Updates

HI everyone thanks for all your submissions so far. Please note the following:

- photos have been uploaded to assist with themes

- background could be a solid colour or texture (e.g. tree trunk texture)

- please use a hand writing font similar to Fontaro font "Lift Our Voice" - doesn't have to be exactly this but similar

Thank you,

Corvel

Hi again everyone

I apologise but the pixel bazaar website won't allow me to upload files. I will attempt to correct this as soon as possible. Thanks                                   

Target Market(s)

18-55 year olds who appreciate this genre of music; gay and lesbian community

Industry/Entity Type

Charity

Requirements
Should not have
• No flowers or flowery themes

```html
<!DOCTYPE html>
<html lang="en">
<head>
<meta charset="utf-8">
<title>Corvel Ashdown — Singer | Songwriter | Performer</title>
<link rel="stylesheet" href="https://fonts.googleapis.com/css2?family=Arimo:wght@400;700&family=Tinos:ital@0;1&display=swap">
<style>
  :root {
    --page-pink: #f1e4ea;
    --band-pink: #e9d5de;
    --ink: #2b2b2b;
    --ink-soft: #555;
    --muted: #8a8a8a;
    --brand-blue: #3a8ad6;
    --link-blue: #2f7fd0;
    --nav-dark: #2a2a2a;
    --nav-text: #8cc8f2;
    --card-bg: #eaf3f8;
    --card-shadow: rgba(0,0,0,0.12);
    --button-dark: #3c3c3c;
    --frame: #ffffff;
    --photo-sky: #a9d3e6;
    --photo-sea: #7fb2cf;
    --photo-warm: #6b4a3a;
    --photo-dark: #2c2622;
  }
  * { box-sizing: border-box; margin: 0; padding: 0; }
  html, body { width: 778px; height: 1200px; overflow: hidden; }
  body {
    position: relative;
    background: var(--page-pink);
    font-family: "Arimo", Arial, sans-serif;
    color: var(--ink);
  }
  .abs { position: absolute; }
  .top-rule, .bottom-rule { position: absolute; left: 0; width: 778px; background: var(--nav-dark); }
  .top-rule { top: 0; height: 4px; }
  .bottom-rule { bottom: 0; height: 6px; }

  /* Header */
  .site-logo {
    left: 86px; top: 44px;
    font-size: 30px; font-weight: 400; letter-spacing: 4px;
    color: var(--brand-blue);
  }
  .social-top { left: 530px; top: 24px; display: flex; gap: 14px; align-items: center; }
  .social-top span { font-size: 11px; font-weight: 700; color: var(--link-blue); }
  .tagline { left: 528px; top: 54px; font-size: 13px; color: var(--ink); letter-spacing: 0.5px; }

  /* Navigation */
  .main-nav {
    position: absolute; left: 0; top: 120px; width: 778px; height: 34px;
    background: linear-gradient(#3b3b3b, #222);
  }
  .main-nav a {
    position: absolute; top: 0; height: 34px; line-height: 34px;
    transform: translateX(-50%);
    font-size: 11px; color: var(--nav-text); text-decoration: none; white-space: nowrap;
  }
  .main-nav a.active {
    top: -4px; height: 40px; line-height: 40px; width: 57px; text-align: center;
    background: var(--brand-blue); color: #fff;
  }

  /* Slider */
  .hero {
    left: 88px; top: 172px; width: 614px; height: 226px;
    border: 3px solid var(--frame);
    background: linear-gradient(180deg, var(--photo-sky) 0%, #cfe6ef 55%, var(--photo-sea) 100%);
    box-shadow: 0 1px 3px var(--card-shadow);
  }
  .hero-arrow {
    position: absolute; top: 104px; width: 18px; height: 18px; border-radius: 50%;
    background: rgba(255,255,255,0.45);
  }
  .hero-arrow svg { display: block; }

  /* Welcome */
  .welcome-band { left: 0; top: 418px; width: 778px; height: 132px; background: var(--band-pink); }
  .serif { font-family: "Tinos", Georgia, serif; font-style: italic; }
  .welcome-kicker { left: 86px; top: 440px; font-size: 13px; }
  .welcome-title { left: 86px; top: 458px; font-size: 20px; }
  .welcome-title em { color: var(--brand-blue); }
  .welcome-text { left: 86px; top: 495px; width: 620px; font-size: 13px; line-height: 19px; color: var(--ink-soft); }

  /* Feature cards */
  .feature-card {
    width: 194px; height: 198px; top: 582px;
    background: var(--card-bg); border-radius: 6px;
    box-shadow: 0 3px 6px var(--card-shadow);
  }
  .card-ribbon { position: absolute; left: 5px; top: -4px; }
  .card-label {
    position: absolute; left: 4px; top: 150px; width: 120px;
    transform: rotate(-90deg); transform-origin: left top;
    font-size: 19px; color: #9a9a9a;
  }
  .card-photo {
    position: absolute; left: 37px; top: 20px; width: 143px; height: 92px;
    border: 3px solid var(--frame);
    background: linear-gradient(135deg, var(--photo-warm), var(--photo-dark));
  }
  .card-text { position: absolute; left: 34px; top: 124px; width: 150px; font-size: 8px; line-height: 10px; color: var(--ink); }
  .card-button {
    position: absolute; left: 33px; top: 167px; width: 50px; height: 19px;
    line-height: 19px; text-align: center; font-size: 9px; color: #fff; font-weight: 700;
    border-radius: 2px; box-shadow: 1px 2px 2px var(--card-shadow);
  }
  .card-button.blue { background: var(--brand-blue); }
  .card-button.dark { background: var(--button-dark); }

  /* Latest update */
  .latest-band { left: 0; top: 802px; width: 778px; height: 242px; background: var(--band-pink); }
  .section-title { font-size: 19px; }
  .section-rule { height: 1px; background: #d8c3cc; }
  .update-item { top: 869px; width: 115px; }
  .update-photo {
    width: 115px; height: 115px; border: 3px solid var(--frame);
    background: linear-gradient(160deg, var(--photo-warm), var(--photo-dark) 70%);
    box-shadow: 0 1px 3px var(--card-shadow);
  }
  .update-caption { margin-top: 7px; font-size: 11px; color: var(--ink); white-space: nowrap; }
  .update-link { display: block; margin-top: 2px; font-size: 7px; color: var(--link-blue); }

  /* Footer */
  .footer-links { font-size: 9px; line-height: 15.5px; }
  .footer-links a { display: block; color: var(--ink); text-decoration: none; }
  .footer-links a.current { color: var(--link-blue); text-decoration: underline; }
  .social-grid { left: 403px; top: 1094px; display: grid; grid-template-columns: repeat(4, 20px); gap: 6px 5px; }
  .social-grid span { width: 20px; height: 20px; border-radius: 4px; }
  .footer-logo { left: 548px; top: 1101px; font-size: 16px; letter-spacing: 2px; color: var(--brand-blue); }
  .copyright { left: 526px; top: 1122px; font-size: 7px; color: var(--muted); }
</style>
</head>
<body>
  <div class="top-rule"></div>

  <header>
    <div class="abs site-logo">CORVEL</div>
    <div class="abs social-top">
      <span>Friendspace</span><span>Chirpline</span><span>VidRelay</span>
    </div>
    <div class="abs tagline">Singer | Songwriter | Performer</div>
  </header>

  <nav class="main-nav">
    <a class="active" href="#" style="left:115px">Home</a>
    <a href="#" style="left:180px">Bio</a>
    <a href="#" style="left:245px">News</a>
    <a href="#" style="left:308px">Gigs</a>
    <a href="#" style="left:373px">Gallery</a>
    <a href="#" style="left:438px">See &amp; Hear</a>
    <a href="#" style="left:503px">Store</a>
    <a href="#" style="left:568px">Generocity</a>
    <a href="#" style="left:632px">Contact</a>
  </nav>

  <div class="abs hero" role="img" aria-label="Photo of the singer smiling with arms raised against a sky and sea background">
    <span class="hero-arrow" style="left:8px">
      <svg width="18" height="18" viewBox="0 0 18 18"><path d="M10.5 5 L6.5 9 L10.5 13" stroke="#fff" stroke-width="2" fill="none"/></svg>
    </span>
    <span class="hero-arrow" style="right:8px">
      <svg width="18" height="18" viewBox="0 0 18 18"><path d="M7.5 5 L11.5 9 L7.5 13" stroke="#fff" stroke-width="2" fill="none"/></svg>
    </span>
  </div>

  <section>
    <div class="abs welcome-band"></div>
    <p class="abs serif welcome-kicker">Welcome to</p>
    <h1 class="abs serif welcome-title" style="font-weight:400">Official Website of <em>Corvel</em> Ashdown</h1>
    <p class="abs serif welcome-text">Female singer / Songwriter and Performer who is launching her debut album this year. She writes and performs folk.... pop.... soft... rock music and plays guitar and piano.</p>
  </section>

  <section>
    <article class="abs feature-card" style="left:88px">
      <svg class="card-ribbon" width="28" height="44" viewBox="0 0 28 44"><path d="M0 0 H28 V44 L14 34 L0 44 Z" fill="#3a8ad6"/></svg>
      <div class="card-label serif">Store</div>
      <div class="card-photo" role="img" aria-label="Portrait photo of the singer"></div>
      <p class="card-text">Our development services related to software are known for implementing the best practices in the industry.</p>
      <span class="card-button blue">More..</span>
    </article>
    <article class="abs feature-card" style="left:299px">
      <svg class="card-ribbon" width="28" height="44" viewBox="0 0 28 44"><path d="M0 0 H28 V44 L14 34 L0 44 Z" fill="#3a8ad6"/></svg>
      <div class="card-label serif">See &amp; Hear</div>
      <div class="card-photo" role="img" aria-label="Portrait photo of the singer"></div>
      <p class="card-text">Our development services related to software are known for implementing the best practices in the industry.</p>
      <span class="card-button dark">More..</span>
    </article>
    <article class="abs feature-card" style="left:510px">
      <svg class="card-ribbon" width="28" height="44" viewBox="0 0 28 44"><path d="M0 0 H28 V44 L14 34 L0 44 Z" fill="#3a8ad6"/></svg>
      <div class="card-label serif">Gallery</div>
      <div class="card-photo" role="img" aria-label="Portrait photo of the singer"></div>
      <p class="card-text">Our development services related to software are known for implementing the best practices in the industry.</p>
      <span class="card-button dark">More..</span>
    </article>
  </section>

  <section>
    <div class="abs latest-band"></div>
    <h2 class="abs serif section-title" style="left:86px; top:821px; font-weight:400">Latest Update</h2>
    <div class="abs section-rule" style="left:86px; top:846px; width:618px"></div>
    <div class="abs update-item" style="left:86px"><div class="update-photo" role="img" aria-label="Photo of the singer playing guitar"></div><p class="update-caption serif">Guitar Performance by</p><a class="update-link serif" href="#">Buy This Album</a></div>
    <div class="abs update-item" style="left:211px"><div class="update-photo" role="img" aria-label="Photo of the singer playing guitar"></div><p class="update-caption serif">Guitar Performance by</p><a class="update-link serif" href="#">Buy This Album</a></div>
    <div class="abs update-item" style="left:336px"><div class="update-photo" role="img" aria-label="Photo of the singer playing guitar"></div><p class="update-caption serif">Guitar Performance by</p><a class="update-link serif" href="#">Buy This Album</a></div>
    <div class="abs update-item" style="left:461px"><div class="update-photo" role="img" aria-label="Photo of the singer playing guitar"></div><p class="update-caption serif">Guitar Performance by</p><a class="update-link serif" href="#">Buy This Album</a></div>
    <div class="abs update-item" style="left:586px"><div class="update-photo" role="img" aria-label="Photo of the singer playing guitar"></div><p class="update-caption serif">Guitar Performance by</p><a class="update-link serif" href="#">Buy This Album</a></div>
  </section>

  <footer>
    <h2 class="abs serif section-title" style="left:86px; top:1064px; font-weight:400">More Links</h2>
    <div class="abs section-rule" style="left:170px; top:1082px; width:534px"></div>
    <div class="abs footer-links" style="left:86px; top:1096px">
      <a class="current" href="#">Home</a><a href="#">About Us</a><a href="#">News</a><a href="#">Gigs</a>
    </div>
    <div class="abs footer-links" style="left:160px; top:1096px">
      <a href="#">Album</a><a href="#">Music</a><a href="#">Videos</a><a href="#">Gallery</a>
    </div>
    <div class="abs footer-links" style="left:226px; top:1096px">
      <a href="#">Store</a><a href="#">Generosity</a><a href="#">Bio</a>
    </div>
    <div class="abs social-grid" aria-label="Social links">
      <span style="background:#3aa7e0"></span><span style="background:#c8302b"></span><span style="background:#3b5a98"></span><span style="background:#1f78b4"></span>
      <span style="background:#b8161f"></span><span style="background:#f2f2f2"></span><span style="background:#49a634"></span><span style="background:#f08a1c"></span>
    </div>
    <div class="abs footer-logo">CORVEL</div>
    <p class="abs copyright">Copyright 2013-14.  All Right Reserved</p>
  </footer>

  <div class="bottom-rule"></div>
</body>
</html>
```